a residential painting contractor I need a 6x9 postcard made

I already have a logo, I'm trying to offer my services to people. you can put that there's a 250$ discount for first time customers. include my License number #4629318 as well as the services I offer, interior and exterior painting, pressure washing, cabinet painting, epoxy floors, wood staining, decks, fences and much more. I'm licensed bonded and insured as well.

Target Market(s)

residential consumers (homeowners)

Industry/Entity Type

Painting contractor

Requirements
Must have
• postage stuff on the back I've linked some pictures top right please, my license number, what I do, phone number (341)572-6190 email brushkelvo7@maplint.com, front and back of postcard
Nice to have
• well lit house in the background, maybe little circles of people doing some of the services I offer

```html
<!DOCTYPE html>
<html lang="en">
<head>
<meta charset="utf-8">
<title>Kelvo Painting – 6x9 Postcard</title>
<link rel="stylesheet" href="https://fonts.googleapis.com/css2?family=Oswald:wght@400;500;600&family=Open+Sans:ital,wght@0,400;0,600;0,700;1,700&family=Merriweather:wght@700&display=swap">
<style>
  :root{
    --ink:#2b2a30;
    --dark:#2e2d35;
    --slate:#6d6b70;
    --mid:#76747a;
    --panel-top:#dad8d6;
    --panel-bottom:#f3f2f0;
    --paper:#ffffff;
    --stage:#dcdcdc;
    --sky:#b9cfe3;
    --stone:#8f857b;
    --lawn:#66704c;
  }
  *{box-sizing:border-box;margin:0;padding:0}
  html,body{width:978px;height:1200px;overflow:hidden}
  body{background:var(--stage);position:relative;font-family:"Open Sans",Arial,sans-serif;color:var(--ink)}
  .card{position:absolute;left:109px;width:760px;height:508px;background:var(--paper);overflow:hidden;box-shadow:0 4px 10px rgba(0,0,0,.25)}
  .card--front{top:58px}
  .card--back{top:620px}
  .abs{position:absolute}

  /* photo areas */
  .photo{position:absolute}
  .photo--house{left:0;top:0;width:497px;height:312px;background:linear-gradient(180deg,var(--sky) 0%,#dfe7ee 22%,#9a9189 40%,var(--stone) 70%,#5d5a52 90%,var(--lawn) 100%)}
  .photo--room{top:318px;height:96px}
  .photo--room-living{left:0;width:124px;background:linear-gradient(180deg,#e4e2de,#b4aea6)}
  .photo--room-deck{left:128px;width:124px;background:linear-gradient(180deg,#cfccc6,#8e939a)}
  .photo--room-kitchen{left:256px;width:60px;background:linear-gradient(180deg,#c3bcb3,#6a6560)}
  .photo--painter{left:312px;top:120px;width:230px;height:388px;background:linear-gradient(180deg,#c8b29e 0%,#c8b29e 18%,#2f3b58 26%,#2f3b58 42%,#f4f4f4 46%,#e4e4e4 100%);border-radius:110px 110px 0 0}
  .photo--before{left:0;top:0;width:193px;height:137px;background:linear-gradient(180deg,#d3dde6 0%,#ecebe8 40%,#d9d8d4 75%,#7d8a6b 100%)}
  .photo--after{left:198px;top:0;width:190px;height:137px;background:linear-gradient(180deg,#d3dde6 0%,#56627a 40%,#4a566b 75%,#6e7c5a 100%)}

  .corner-tag{position:absolute;top:10px;font:600 11px "Oswald",sans-serif;color:var(--ink);background:var(--paper);padding:2px 18px;transform:rotate(-45deg)}

  /* brand name stand-in */
  .logo-box{left:12px;top:0;width:126px;height:122px;background:var(--paper);border-radius:0 0 14px 14px;display:flex;align-items:center;justify-content:center}
  .brand-name{font:600 22px/1.05 "Oswald",sans-serif;color:var(--ink);text-align:center;letter-spacing:.5px}

  /* front right panel */
  .services-panel{left:497px;top:0;width:263px;height:508px;background:linear-gradient(180deg,var(--panel-top),var(--panel-bottom))}
  .headline{right:20px;top:18px;text-align:right;font:500 27px/1.12 "Oswald",sans-serif;color:var(--ink)}
  .pill{background:var(--slate);color:var(--paper);font:500 21px/30px "Oswald",sans-serif;height:30px}
  .pill--services{left:552px;top:85px;width:208px;border-radius:15px 0 0 15px;padding-left:22px}
  .service-list{right:14px;top:122px;list-style:none}
  .service-list li{display:flex;align-items:center;justify-content:flex-end;gap:8px;height:28px;font:500 17px "Oswald",sans-serif;color:var(--ink)}
  .service-icon{width:24px;height:24px;background:var(--slate);border-radius:4px;display:flex;align-items:center;justify-content:center}
  .license{font:italic 700 9px "Open Sans",sans-serif;color:var(--ink);z-index:2}
  .license--front{right:16px;top:350px}

  .offer-band{left:497px;top:358px}
  .offer-front{left:540px;top:438px;display:flex;align-items:center;gap:8px;color:var(--paper);z-index:2}
  .offer-amount{font:500 52px/1 "Oswald",sans-serif}
  .offer-text{font:500 10.5px/1.2 "Oswald",sans-serif;text-transform:uppercase;width:100px}

  /* contact band */
  .contact-band{left:0;top:419px;width:468px;height:89px;background:var(--mid)}
  .contact{left:14px;color:var(--paper)}
  .contact__licensed{font:700 14px "Merriweather",serif;color:#e1e0e0}
  .contact__estimate{display:flex;align-items:center;gap:10px;font:500 19px "Oswald",sans-serif;margin-top:2px}
  .contact__email{display:flex;align-items:center;gap:6px;font:400 12.5px "Open Sans",sans-serif;margin-top:1px}
  .dot{width:8px;height:8px;border-radius:50%;background:var(--paper)}

  /* back */
  .quote-panel{left:0;top:137px;width:388px;height:260px;background:linear-gradient(180deg,#d4d2d1,var(--panel-bottom))}
  .pill--quote{left:0;top:149px;width:234px;border-radius:0 15px 15px 0;padding-left:22px;font-size:19px}
  .about{left:30px;top:188px;width:340px;font:400 12.6px/1.5 "Open Sans",sans-serif;color:var(--ink)}
  .about b{font-weight:700}
  .offer-box{left:22px;top:256px;width:331px;height:86px;border:1.5px dashed #8d8b8e;border-radius:8px;display:flex;align-items:center;gap:10px}
  .offer-box__tab{width:26px;height:84px;background:var(--slate);border-radius:6px 0 0 6px;display:flex;align-items:center;justify-content:center}
  .offer-box__tab span{transform:rotate(-90deg);color:var(--paper);font:500 15px "Oswald",sans-serif;letter-spacing:1px}
  .offer-box .offer-amount{color:var(--ink);font-size:56px}
  .offer-box .offer-text{color:var(--ink);font-size:11px;width:112px}
  .tagline{left:0;width:388px;top:352px;text-align:center;font:italic 700 14.5px "Open Sans",sans-serif}
  .license--back{left:0;width:388px;top:375px;text-align:center}
  .quote-band{left:0;top:368px}

  .logo-back{left:429px;top:16px;width:117px;height:108px;display:flex;align-items:center;justify-content:center}
  .postage{left:643px;top:23px;width:91px;height:88px;border:1px solid #444;font:400 11px/1.25 Arial,sans-serif;text-align:center;padding-top:6px;color:#111}
  .address{left:494px;top:157px;width:240px;height:93px;border:1px solid #444;font:400 13px/1.25 Arial,sans-serif;color:#111}
  .address__line{position:absolute;right:18px;top:8px;font-size:9px}
  .address__to{position:absolute;left:14px;top:38px}
</style>
</head>
<body>

<!-- FRONT -->
<section class="card card--front">
  <div class="photo photo--house" role="img" aria-label="Photo of a large stone and siding two-storey house with landscaped front lawn"></div>
  <div class="abs logo-box"><span class="brand-name">KELVO<br>PAINTING</span></div>
  <div class="photo photo--room photo--room-living" role="img" aria-label="Photo of a freshly painted living room interior"></div>
  <div class="photo photo--room photo--room-deck" role="img" aria-label="Photo of a painted deck patio with outdoor furniture"></div>
  <div class="photo photo--room photo--room-kitchen" role="img" aria-label="Photo of a renovated kitchen with painted cabinets"></div>

  <div class="abs services-panel"></div>
  <h1 class="abs headline">GIVE YOUR HOME<br>NEW LIFE!</h1>
  <div class="abs pill pill--services">OUR SERVICES:</div>
  <ul class="abs service-list">
    <li>INTERIOR PAINTING<span class="service-icon"><svg width="14" height="14" viewBox="0 0 14 14"><rect x="2" y="1" width="10" height="5" rx="1" fill="#fff"/><rect x="6" y="6" width="2" height="7" fill="#fff"/></svg></span></li>
    <li>EXTERIOR PAINTING<span class="service-icon"><svg width="14" height="14" viewBox="0 0 14 14"><path d="M1 7 7 1l6 6v6H1z" fill="#fff"/></svg></span></li>
    <li>PRESSURE WASHING<span class="service-icon"><svg width="14" height="14" viewBox="0 0 14 14"><rect x="3" y="4" width="8" height="9" rx="1" fill="#fff"/><rect x="5" y="1" width="4" height="3" fill="#fff"/></svg></span></li>
    <li>CABINET PAINTING<span class="service-icon"><svg width="14" height="14" viewBox="0 0 14 14"><rect x="2" y="1" width="10" height="12" fill="none" stroke="#fff" stroke-width="1.6"/><rect x="8" y="6" width="2" height="2" fill="#fff"/></svg></span></li>
    <li>EPOXY FLOORS<span class="service-icon"><svg width="14" height="14" viewBox="0 0 14 14"><path d="M7 1l6 6-6 6-6-6z" fill="#fff"/></svg></span></li>
    <li>WOOD STAINING<span class="service-icon"><svg width="14" height="14" viewBox="0 0 14 14"><path d="M2 9 9 2l3 3-7 7H2z" fill="#fff"/></svg></span></li>
    <li>DECK PAINTING<span class="service-icon"><svg width="14" height="14" viewBox="0 0 14 14"><rect x="5" y="1" width="4" height="7" fill="#fff"/><rect x="6" y="8" width="2" height="5" fill="#fff"/></svg></span></li>
    <li>FENCE PAINTING<span class="service-icon"><svg width="14" height="14" viewBox="0 0 14 14" fill="#fff"><rect x="2" y="2" width="2" height="11"/><rect x="6" y="2" width="2" height="11"/><rect x="10" y="2" width="2" height="11"/><rect x="1" y="5" width="12" height="1.5"/><rect x="1" y="9" width="12" height="1.5"/></svg></span></li>
  </ul>
  <p class="abs license license--front">License number #4629318</p>

  <svg class="abs offer-band" width="263" height="150" viewBox="0 0 263 150">
    <path d="M0 72 Q130 40 263 16" fill="none" stroke="#b9b7b8" stroke-width="5"/>
    <path d="M0 82 Q130 52 263 28 L263 150 L0 150Z" fill="var(--dark)"/>
  </svg>

  <div class="abs contact-band"></div>
  <div class="photo photo--painter" role="img" aria-label="Photo of a smiling painter in a navy shirt and white apron holding a brush and paint can"></div>

  <div class="abs offer-front">
    <span class="offer-amount">250$</span>
    <span class="offer-text">Discount for first time customers on whole interior or exterior repaints</span>
  </div>

  <div class="abs contact" style="top:430px">
    <p class="contact__licensed">Licensed Bonded &amp; Insured</p>
    <p class="contact__estimate">FREE ESTIMATE!
      <svg width="16" height="18" viewBox="0 0 16 18"><rect x="3" y="1" width="10" height="16" rx="2" fill="none" stroke="#fff" stroke-width="2"/><rect x="6" y="13" width="4" height="2" fill="#fff"/></svg>
      (341) 572-6190</p>
    <p class="contact__email"><span class="dot"></span>brushkelvo7@maplint.com</p>
  </div>
</section>

<!-- BACK -->
<section class="card card--back">
  <div class="photo photo--before" role="img" aria-label="Before photo of a white two-storey house with worn paint"></div>
  <div class="photo photo--after" role="img" aria-label="After photo of the same house freshly painted dark blue-gray"></div>
  <span class="corner-tag" style="left:-16px">BEFORE</span>
  <span class="corner-tag" style="left:183px">AFTER</span>

  <div class="abs quote-panel"></div>
  <div class="abs pill pill--quote">SCHEDULE A FREE QUOTE</div>
  <p class="abs about"><b>KELVO PAINTING</b> is a professional, efficient and client focused painting company. Our goal is to leave you feeling great and your home looking its best!</p>
  <div class="abs offer-box">
    <div class="offer-box__tab"><span>OFFER</span></div>
    <span class="offer-amount">250$</span>
    <span class="offer-text">Discount for first time customers on whole interior or exterior repaints</span>
  </div>
  <p class="abs tagline">No project is too large or too small.</p>

  <svg class="abs quote-band" width="388" height="140" viewBox="0 0 388 140">
    <path d="M0 30 Q200 72 388 14 L388 140 L0 140Z" fill="var(--paper)"/>
    <path d="M0 44 Q200 86 388 28 L388 140 L0 140Z" fill="var(--dark)"/>
  </svg>
  <p class="abs license license--back">License number #4629318</p>

  <div class="abs contact" style="top:428px">
    <p class="contact__licensed">Licensed Bonded &amp; Insured</p>
    <p class="contact__estimate">FREE ESTIMATE!
      <svg width="16" height="18" viewBox="0 0 16 18"><rect x="3" y="1" width="10" height="16" rx="2" fill="none" stroke="#fff" stroke-width="2"/><rect x="6" y="13" width="4" height="2" fill="#fff"/></svg>
      (341) 572-6190</p>
    <p class="contact__email"><span class="dot"></span>brushkelvo7@maplint.com</p>
  </div>

  <div class="abs logo-back"><span class="brand-name">KELVO<br>PAINTING</span></div>
  <div class="abs postage">PRSRT STD<br>ECRWSS<br>U.S. Postage<br><b>PAID</b><br>EDDM RETAIL</div>
  <div class="abs address">
    <span class="address__line">*****************ECRWSS****</span>
    <span class="address__to">Local<br>Postal Customer</span>
  </div>
</section>

</body>
</html>
```